New Design for our Velorin Gran Reserva Brandy, it is the label design for the bottle label

We need a new bottle label for our Brandy Gran Reserva that we want to bring to the market.

Please have a look at all our current bottles and labels and the feel of our company under www.velorin-example.ch

The bottle that we will be using for the brand is a different one than the one that we already have, the design of the bottle is attached with a document.

I have also attached a briefing in regards to Brandy in general for your information.

### 1. What is Brandy?
Brandy is a distilled spirit made from fermented wine or other fruit wines. It is traditionally aged in oak barrels, which gives it its characteristic color and rich flavor. The aging process in oak is essential for developing the aromas and quality of the brandy.

### 2. What is Brandy Reserva?
A Brandy labeled as "Reserva" has undergone a longer aging process, typically at least 2 to 3 years, in oak barrels. This aging gives the brandy a deeper, more complex flavor profile and a darker color. "Reserva" is often an indication of higher quality.

### 3. Who enjoys drinking Brandy?
Brandy is typically favored by those who appreciate a deep, rich tasting experience. This often includes older consumers who value the time-aged complexity of the spirit. However, Brandy is also gaining popularity among younger people, especially through cocktails and modern serving styles.

### 4. Why is Brandy trending?
Brandy is experiencing a resurgence as consumers increasingly value quality and artisanal production methods. Its versatility in cocktails and association with traditional, luxurious experiences have also contributed to its renewed popularity.

### 5. What colors would be associated with Brandy?
The typical colors associated with Brandy are warm gold, amber, and deep golden-brown tones. These colors reflect the aging process in oak barrels and the richness of the flavors. Other associated colors might include dark brown and mahogany.

### 6. What is important to customers when buying Brandy?
Customers care about the origin of the Brandy, the aging time, the quality of the ingredients, the production method, and the brand. They also pay attention to the prestige of the product and the authenticity of the production.

### 7. What is not important to customers when buying Brandy?
For many customers, the price and packaging (unless it’s especially exclusive) may be less important than the quality and taste of the Brandy. The distillery name might be less significant if it isn’t tied to a particular reputation.

### 8. What do customers know about Swiss Brandy?
Swiss Brandy is still relatively unknown in many markets, but customers who are familiar with it appreciate the precision and quality of Swiss production. Swiss Brandy is assumed to be made with care and under strict quality standards.

### 9. What is Brandy Gran Reserva?
**Brandy Gran Reserva** is an even higher quality and longer-aged version of Brandy. Generally, a Gran Reserva is aged for at least 5 to 10 years or more in oak barrels. This extended aging process gives the Brandy an especially deep, complex flavor profile and often a darker, richer color. Gran Reserva is often regarded as the top-tier product within a Brandy range and appeals to discerning consumers who value quality, refinement, and a luxurious tasting experience.

The label “Gran Reserva” thus indicates the highest quality level for Brandies, similar to other spirits (like wine or whisky), where the aging time is a critical factor.

### 10. What emotions are associated with Brandy?
Brandy is often associated with luxury, relaxation, and comfort. It evokes feelings of tradition, elegance, and sophistication. Drinking Brandy is frequently seen as a moment of reflection and enjoyment.

### 11. How should Brandy be marketed?
Brandy should be marketed with a focus on its artisanal production, quality, and tradition. A narrative around the product, its aging, and origin can help create an emotional connection with the customer. The marketing should also emphasize the versatility of Brandy, whether consumed neat or in cocktails.

### 12. Sales test and label design for Velorin Brandy
For a sales test, I would suggest a tasting in an upscale setting, perhaps paired with a storytelling presentation highlighting the history of the 6-year aged Brandy and its aging in oak barrels.

**Label design**:
The label should reflect the exclusivity of the product, with an elegant, minimalist design. Colors like deep gold, mahogany, and a hint of deep blue could be used to emphasize the aging and quality of the Brandy. The label should include information about the aging time, the use of oak barrels, and a brief story about the Brandy’s production. A seal or embossing highlighting the craftsmanship would also be fitting.

Target Market(s)

Customers that like Brandy

Requirements
Must have
• the Alcohol % must be included on the label as well as our address.

```html
<!DOCTYPE html>
<html lang="en">
<head>
<meta charset="utf-8">
<title>Velorin Gran Reserva Brandy – Bottle Label</title>
<link rel="stylesheet" href="https://fonts.googleapis.com/css2?family=Libre+Caslon+Text:wght@400;700&family=Mrs+Saint+Delafield&display=swap">
<style>
  :root {
    --mahogany: #4f2c1f;
    --gold: #c9a35a;
    --gold-light: #e6c47a;
    --gold-dark: #7d6230;
    --navy: #1d2556;
    --swiss-red: #e30613;
    --cream: #f6efe3;
    --page: #ffffff;
  }
  * { margin: 0; padding: 0; box-sizing: border-box; }
  html, body {
    width: 1200px; height: 1200px; overflow: hidden;
    background: var(--page);
  }
  .canvas { position: relative; width: 1200px; height: 1200px; }
  .label {
    position: absolute; left: 316px; top: 50px;
    width: 568px; height: 1100px;
    font-family: "Libre Caslon Text", Georgia, serif;
    color: var(--cream);
  }
  .label-shape { position: absolute; inset: 0; }
  .swiss-flag { position: absolute; left: 253px; top: 149px; width: 62px; height: 41px; }
  .brand-name {
    position: absolute; left: 0; right: 0; top: 232px;
    text-align: center; font-weight: 700; font-size: 70px; line-height: 1;
    letter-spacing: -1px; color: #fff;
  }
  .brand-type {
    position: absolute; left: 0; right: 0; top: 311px;
    text-align: center; font-weight: 700; font-size: 16px;
    letter-spacing: 7px; padding-left: 7px; color: #fff;
  }
  .edition {
    position: absolute; left: 0; right: 0; top: 365px;
    text-align: center; font-family: "Mrs Saint Delafield", cursive;
    font-size: 52px; line-height: 1; color: var(--gold); letter-spacing: 3px;
  }
  .seal {
    position: absolute; left: 175px; top: 459px; width: 218px; height: 218px;
    border-radius: 50%; background: var(--navy);
    display: flex; align-items: center; justify-content: center;
  }
  .seal-name {
    font-weight: 700; font-size: 30px; letter-spacing: 4px; color: var(--gold);
  }
  .age-block { position: absolute; left: 37px; top: 808px; width: 128px; }
  .age-word {
    font-weight: 700; font-size: 29px; line-height: 1; color: #fff;
    display: flex; justify-content: space-between;
  }
  .age-number {
    font-size: 104px; line-height: 0.82; margin: 4px 0 4px -4px;
    color: var(--navy); -webkit-text-stroke: 1.4px var(--gold);
    letter-spacing: -4px;
  }
  .age-years { letter-spacing: 2px; }
  .divider-v {
    position: absolute; left: 170px; top: 792px; width: 1px; height: 185px;
    background: var(--gold);
  }
  .divider-h {
    position: absolute; left: 37px; top: 954px; width: 515px; height: 1px;
    background: linear-gradient(90deg, var(--gold-dark), var(--gold), var(--gold-dark));
  }
  .story { position: absolute; left: 176px; top: 794px; width: 356px; }
  .story-kicker {
    font-weight: 700; font-size: 17px; letter-spacing: 4px; color: #fff; line-height: 1;
  }
  .story-title {
    margin-top: 9px; padding-bottom: 3px; white-space: nowrap;
    border-bottom: 1px solid var(--gold);
    font-weight: 700; font-size: 11px; line-height: 1.2; letter-spacing: 0.6px; color: #fff;
  }
  .story-text {
    margin-top: 4px; font-size: 8.6px; line-height: 9.6px;
    text-align: justify; hyphens: auto; color: #fff;
  }
  .facts {
    position: absolute; left: 170px; top: 926px; width: 382px; height: 28px;
    border-top: 1px solid var(--gold); display: flex;
  }
  .facts span {
    flex: 0 0 auto; display: flex; align-items: center; justify-content: center;
    font-size: 14px; color: #fff; border-right: 1px solid var(--gold);
  }
  .facts .volume { width: 111px; }
  .facts .strength { width: 114px; }
  .facts .bottle-no { border-right: none; justify-content: flex-start; padding-left: 7px; flex: 1; }
</style>
</head>
<body>
<main class="canvas">
  <section class="label" aria-label="Velorin Gran Reserva Brandy bottle label">
    <svg class="label-shape" viewBox="0 0 568 1100" width="568" height="1100" aria-hidden="true">
      <defs>
        <linearGradient id="goldFrame" x1="0" y1="0" x2="0" y2="1">
          <stop offset="0" stop-color="#e6c47a"/>
          <stop offset="0.5" stop-color="#6e5529"/>
          <stop offset="1" stop-color="#a8853f"/>
        </linearGradient>
        <linearGradient id="goldBase" x1="0" y1="0" x2="1" y2="0">
          <stop offset="0" stop-color="#7d6230"/>
          <stop offset="0.5" stop-color="#f0cf85"/>
          <stop offset="1" stop-color="#7d6230"/>
        </linearGradient>
      </defs>
      <polygon points="284,0 568,191 568,1100 0,1100 0,191" fill="#4f2c1f"/>
      <polyline points="19,1073 19,208 284,27 552,208 552,1073" fill="none" stroke="url(#goldFrame)" stroke-width="3"/>
      <line x1="19" y1="1073" x2="552" y2="1073" stroke="url(#goldBase)" stroke-width="4"/>
    </svg>

    <svg class="swiss-flag" viewBox="0 0 62 41" aria-label="Swiss flag" role="img">
      <rect width="62" height="41" fill="#e30613"/>
      <rect x="27" y="9" width="8" height="23" fill="#fff"/>
      <rect x="19.5" y="16.5" width="23" height="8" fill="#fff"/>
    </svg>

    <h1 class="brand-name">VELORIN</h1>
    <p class="brand-type">BRANDY</p>
    <p class="edition">Gran Reserva</p>

    <div class="seal"><span class="seal-name">VELORIN</span></div>

    <div class="age-block">
      <div class="age-word"><span>A</span><span>G</span><span>E</span><span>D</span></div>
      <div class="age-number">06</div>
      <div class="age-word age-years">YEARS</div>
    </div>
    <div class="divider-v"></div>

    <div class="story">
      <p class="story-kicker">OAK BARRELS</p>
      <p class="story-title">HISTORY ABOUT THE BRANDY’S PRODUCTION</p>
      <p class="story-text" lang="de">In unserem historischen Käsereigebäude von 1904 lebt die Tradition der Veredelung hochwertiger Rohstoffe weiter. Einst stand die Käseherstellung im Mittelpunkt, heute sind es die edlen Whiskys, Spirits, Vieilles und Grappas von Velorin, die unsere Passion widerspiegeln. Unser Handwerk basiert auf der ursprünglichen Methode des Brennens mit Holz, umgesetzt in zwei speziell für uns gefertigten Brennblasen. Unser Destillierprozess vereint tiefe Kenntnisse mit moderner Innovation.</p>
    </div>

    <div class="facts">
      <span class="volume">50 cL</span>
      <span class="strength">42% VOL</span>
      <span class="bottle-no">BOTTLE Nº</span>
    </div>
    <div class="divider-h"></div>
  </section>
</main>
</body>
</html>
```